Radiology Department needs a series of 3 facebook posts - similar design

We need a series of 3 posts for our facebook page, each one presenting the activity of one of 3 physicians.
The main design elements can be the same, the only thing that will change between posts will be the field of activity and name of the physician and the representative image of its activity.
If needed the design elements can be slightly different between posts for better adjustment to the representative images.
You can find as an attachment:
- Manual of institutional identity of the Hospital (Velmor Clinica)
- Our facebook cover page
- Our department video
- The representative images for each post, identified with the name of each physician
- The Institutional identity manual with the logo of "Brisa Medical School" - just for Dr Tomas Brandilo post.
So, each one of the three posts should state the name and field of activity of each physician, including somehow the corresponding representative image, and should have background innovative design elements.
Post 1:
Name of the physician: Prof. Doutor Rui Castelvo
Field of activity: Imagiologia Reumatológica e do Sistema Músculo-Esquelético
Image as an attachment
Post 2:
Name of the physician: Prof.ª Doutora Inês Barroca
Field of activity: Imagiologia Cardíaca
Image as an attachment
Post 3:
Name of the physician: Dr. Tomas Lupo
Field of activity: Tese de Doutoramento em Curso - Identificação da Lesão Cartilagínea Precoce. Com orientação do Prof. Doutor Rui Castelvo e Prof.ª Doutora Inês Sofia Carvalhal.
Image as an attachment
Just for Dr Tomas Lupo, the logo of Brisa Medical School should also be included (please check the corresponding institutional identity manual that was just added in documents).
Updates

Just for Dr Tomas Brandilo, the logo of Brisa Medical School should also be included (please check the corresponding institutional identity manual that was just added in documents).

Please note that we are just looking for 3 facebook POSTS, not facebook cover page, thanks.

Please kindly note that we are looking for facebook POST and NOT facebook cover page.

Target Market(s)

General Population

Industry/Entity Type

Health

Font styles to use
Other font styles liked:
• Check manual of institutional identity and try to approach if appropriate

Requirements
Must have
• Check project description.
Nice to have
• If the designer finds appropriate, the logo of the Hospital would be nice in all the three posts, the most simple one just stating "VelmorClinica" - please check the attached manual of institutional identity

```html
<!DOCTYPE html>
<html lang="pt">
<head>
<meta charset="utf-8">
<title>VelmorClinica — Radiologia, série de posts</title>
<link rel="stylesheet" href="https://fonts.googleapis.com/css2?family=Roboto:wght@300;400;700&family=Roboto+Condensed:wght@400&display=swap">
<style>
:root{
  --board:#121212;
  --board-edge:#070707;
  --white:#ffffff;
  --ink:#666666;
  --rule:#cfcfcf;
  --teal:#06606f;
  --teal-deep:#0a4a56;
  --amber:#f9b233;
  --silver:#c9c8c9;
  --scan-black:#000000;
  --note:#4a4a4a;
}
*{margin:0;padding:0;box-sizing:border-box}
html,body{width:1200px;height:1027px;overflow:hidden}
body{
  background:radial-gradient(ellipse at 50% 45%,#1c1c1c 0%,var(--board) 55%,var(--board-edge) 100%);
  font-family:"Roboto",Arial,sans-serif;
  position:relative;
}
.post{
  position:absolute;
  width:732px;height:732px;
  transform:scale(.5792);
  transform-origin:0 0;
  overflow:hidden;
  background:var(--white);
}
.post--fetal{left:157.5px;top:48px}
.post--hand{left:629.5px;top:48px}
.post--cartilage{left:157.5px;top:511px}
.post--cardiac{left:629.5px;top:511px}

.post__art{position:absolute;left:0;top:0;width:732px;height:732px}

.portrait{
  position:absolute;left:68px;top:250px;width:180px;height:258px;
  background:linear-gradient(180deg,#3b3b3f 0%,#23252c 45%,#2c2f38 72%,rgba(255,255,255,0) 100%);
  border-radius:70px 70px 0 0;
}

.doctor{position:absolute;left:38px;width:320px;color:var(--ink);z-index:1}
.doctor__name{
  font-weight:700;font-size:38px;line-height:44px;letter-spacing:.2px;
}
.doctor__rule{position:absolute;left:38px;width:280px;height:2px;background:var(--rule)}
.doctor__field{
  position:absolute;left:38px;width:320px;color:var(--ink);
  font-weight:300;font-size:22px;line-height:26px;
}
.doctor__note{
  position:absolute;left:38px;width:300px;color:var(--ink);
  font-weight:700;font-size:17px;line-height:21px;
}

.brand{position:absolute;left:401px;top:612px;width:325px;height:100px}
.brand__dot{
  position:absolute;left:0;top:0;width:66px;height:66px;border-radius:50%;
  background:var(--white);
}
.brand__name{
  position:absolute;left:72px;top:10px;
  font-weight:700;font-size:38px;line-height:44px;color:var(--white);
  white-space:nowrap;
}
.brand__tagline{
  position:absolute;left:72px;top:64px;
  font-family:"Roboto Condensed","Arial Narrow",sans-serif;
  font-size:18px;line-height:22px;color:var(--white);white-space:nowrap;
}

.board-note{
  position:absolute;left:0;width:1200px;top:979px;text-align:center;
  font-weight:700;font-size:22px;color:var(--note);letter-spacing:.3px;
}
</style>
</head>
<body>

<!-- Post: fetal MRI -->
<section class="post post--fetal">
  <svg class="post__art" viewBox="0 0 732 732">
    <defs>
      <radialGradient id="scan-fetal" cx="62%" cy="38%" r="55%">
        <stop offset="0" stop-color="#8a8a8a"/>
        <stop offset=".45" stop-color="#4a4a4a"/>
        <stop offset="1" stop-color="#000"/>
      </radialGradient>
    </defs>
    <rect x="363" y="0" width="369" height="732" fill="var(--teal-deep)"/>
    <polygon points="363,472 476,585 732,332 732,732 363,732" fill="var(--teal)"/>
    <polygon points="0,77 363,440 363,475 0,112" fill="var(--silver)"/>
    <polygon points="0,42 490,532 475,547 0,77" fill="var(--amber)"/>
    <polygon role="img" aria-label="Imagem de ressonância magnética fetal em corte sagital" points="0,0 732,0 732,280 485,527 0,42" fill="url(#scan-fetal)"/>
  </svg>
  <div class="doctor" style="top:555px"><h2 class="doctor__name">Dr. Duarte<br>Reis Valença</h2></div>
  <div class="doctor__rule" style="top:646px"></div>
  <p class="doctor__field" style="top:650px">Ressonância Magnética Fetal<br>Neurorradiologia Pediátrica</p>
  <div class="brand"><span class="brand__dot"></span><span class="brand__name">VelmorClinica</span><span class="brand__tagline">Construímos relações de confiança</span></div>
</section>

<!-- Post: musculoskeletal imaging -->
<section class="post post--hand">
  <svg class="post__art" viewBox="0 0 732 732">
    <defs>
      <radialGradient id="scan-hand" cx="65%" cy="30%" r="55%">
        <stop offset="0" stop-color="#b8b8b8"/>
        <stop offset=".5" stop-color="#5a5a5a"/>
        <stop offset="1" stop-color="#000"/>
      </radialGradient>
    </defs>
    <rect x="363" y="0" width="369" height="732" fill="var(--teal-deep)"/>
    <polygon points="363,472 476,585 732,332 732,732 363,732" fill="var(--teal)"/>
    <polygon points="0,77 363,440 363,475 0,112" fill="var(--silver)"/>
    <polygon points="0,42 490,532 475,547 0,77" fill="var(--amber)"/>
    <polygon points="0,0 732,0 732,280 485,527 0,42" fill="var(--scan-black)"/>
    <polygon role="img" aria-label="Angiografia por ressonância magnética das mãos" points="300,0 732,0 732,280 485,527 300,342" fill="url(#scan-hand)"/>
  </svg>
  <div class="portrait" role="img" aria-label="Retrato do Prof. Doutor Rui Castelvo"></div>
  <div class="doctor" style="top:514px"><h2 class="doctor__name">Prof. Doutor<br>Rui Castelvo</h2></div>
  <div class="doctor__rule" style="top:611px"></div>
  <p class="doctor__field" style="top:624px">Imagiologia Reumatológica<br>e do Sistema<br>Músculo-Esquelético</p>
  <div class="brand"><span class="brand__dot"></span><span class="brand__name">VelmorClinica</span><span class="brand__tagline">Construímos relações de confiança</span></div>
</section>

<!-- Post: cartilage research -->
<section class="post post--cartilage">
  <svg class="post__art" viewBox="0 0 732 732">
    <defs>
      <radialGradient id="scan-cartilage" cx="58%" cy="40%" r="60%">
        <stop offset="0" stop-color="#0b1fa8"/>
        <stop offset=".55" stop-color="#1a3ee0"/>
        <stop offset=".85" stop-color="#0c1a80"/>
        <stop offset="1" stop-color="#000"/>
      </radialGradient>
    </defs>
    <rect x="363" y="0" width="369" height="732" fill="var(--teal-deep)"/>
    <polygon points="363,472 476,585 732,332 732,732 363,732" fill="var(--teal)"/>
    <polygon points="0,77 363,440 363,475 0,112" fill="var(--silver)"/>
    <polygon points="0,42 490,532 475,547 0,77" fill="var(--amber)"/>
    <polygon points="0,0 732,0 732,280 485,527 0,42" fill="var(--scan-black)"/>
    <polygon role="img" aria-label="Mapa paramétrico colorido de cartilagem do joelho" points="160,0 732,0 732,280 485,527 160,202" fill="url(#scan-cartilage)"/>
  </svg>
  <div class="doctor" style="top:488px"><h2 class="doctor__name">Dr. Tomas Lupo</h2></div>
  <div class="doctor__rule" style="top:534px"></div>
  <p class="doctor__field" style="top:540px">Tese de Doutoramento em<br>Curso - Identificação da Lesão<br>Cartilagínea Precoce</p>
  <p class="doctor__note" style="top:637px">Com orientação do Prof. Doutor<br>Rui Castelvo e Prof. Doutora<br>Inês Sofia Carvalhal.</p>
  <div class="brand"><span class="brand__dot"></span><span class="brand__name">VelmorClinica</span><span class="brand__tagline">Construímos relações de confiança</span></div>
</section>

<!-- Post: cardiac imaging -->
<section class="post post--cardiac">
  <svg class="post__art" viewBox="0 0 732 732">
    <defs>
      <radialGradient id="scan-cardiac" cx="60%" cy="38%" r="50%">
        <stop offset="0" stop-color="#a8a8a8"/>
        <stop offset=".5" stop-color="#505050"/>
        <stop offset="1" stop-color="#000"/>
      </radialGradient>
    </defs>
    <rect x="363" y="0" width="369" height="732" fill="var(--teal-deep)"/>
    <polygon points="363,472 476,585 732,332 732,732 363,732" fill="var(--teal)"/>
    <polygon points="0,77 363,440 363,475 0,112" fill="var(--silver)"/>
    <polygon points="0,42 490,532 475,547 0,77" fill="var(--amber)"/>
    <polygon role="img" aria-label="Ressonância magnética cardíaca em corte de quatro câmaras" points="0,0 732,0 732,280 485,527 0,42" fill="url(#scan-cardiac)"/>
  </svg>
  <div class="doctor" style="top:528px"><h2 class="doctor__name">Prof. Doutora<br>Inês Barroca</h2></div>
  <div class="doctor__rule" style="top:617px"></div>
  <p class="doctor__field" style="top:624px">Ressonância Magnética<br>Cardíaca com Stress<br>Farmacológico</p>
  <div class="brand"><span class="brand__dot"></span><span class="brand__name">VelmorClinica</span><span class="brand__tagline">Construímos relações de confiança</span></div>
</section>

<p class="board-note">*This Mock-up is for presentation purposes only</p>

</body>
</html>
```